Stationery Required - Own Logo provided

Hi,

We are a retail company called 'Bramwick Carto Limited' based in the UK and would like some corporate stationery designed.

We have provided our Logo which we would like to use (Its attached to this brief)...

The designs must be orginal, professional, stylish and interesting!

Target Market(s)

We will use this stationery to communicate with our wholesale suppliers and employees, so it must have a 'professional' feel about it.

Industry/Entity Type

It Company

Requirements
Must have
• Must be professional, corporate, stylish and not to 'fussy'. we require ... Business card design, a4 letter, compliment slip. All designs must be supplied in a format where the text (address/telephone numbers etc..) can be edited, as we have alot of staff and operate out of several different premises.
Nice to have
• I would like a windows backround picture file supplied as well so we can integrate that onto our computer systems.

```html
<!DOCTYPE html>
<html lang="en">
<head>
<meta charset="utf-8">
<title>Bramwick Carto Limited – Stationery Set</title>
<link rel="stylesheet" href="https://fonts.googleapis.com/css2?family=Questrial&display=swap">
<style>
  :root {
    --green: #8cc63f;
    --green-bright: #9dd21f;
    --green-deep: #5f9a1c;
    --green-pale: #dcedc2;
    --green-mist: #e8f3d8;
    --ink-green: #6aa321;
    --paper: #ffffff;
    --backdrop: #ecece8;
    --font: "Questrial", "Century Gothic", sans-serif;
  }
  * { box-sizing: border-box; margin: 0; padding: 0; }
  html, body { width: 1200px; height: 781px; overflow: hidden; }
  body { background: var(--backdrop); font-family: var(--font); position: relative; }

  .piece { position: absolute; background: var(--paper); overflow: hidden; box-shadow: 0 2px 6px rgba(0,0,0,.18); }

  /* brand name lockup */
  .brand { display: flex; align-items: center; gap: 6px; color: var(--ink-green); }
  .brand__mark { width: 18px; height: 18px; background: var(--ink-green); flex: none; }
  .brand__text { line-height: 1; }
  .brand__name { display: block; font-size: 26px; letter-spacing: -.5px; }
  .brand__suffix { display: block; font-size: 9px; letter-spacing: 6px; text-transform: uppercase; margin-top: 1px; }

  /* business card fronts */
  .card-front {
    background: linear-gradient(to bottom, var(--green) 0%, #c6e391 28%, #fff 44%, #fff 56%, #bfe08a 74%, #78b62a 100%);
    display: flex; align-items: center; justify-content: center;
  }
  .card-front--square { left: 32px; top: 68px; width: 316px; height: 200px; }
  .card-front--round { left: 4px; top: 462px; width: 286px; height: 160px; border-radius: 30px; }

  /* business card backs */
  .card-back { display: flex; }
  .card-back--square { left: 120px; top: 250px; width: 330px; height: 186px; }
  .card-back--round { left: 146px; top: 580px; width: 296px; height: 158px; border-radius: 30px; }
  .card-back__band {
    position: absolute; left: 12px; top: 72px; width: 160px; height: 32px;
    background: var(--green-pale); display: flex; align-items: center; padding-left: 6px;
  }
  .card-back--round .card-back__band { left: 10px; top: 64px; width: 142px; height: 28px; }
  .card-back__panel {
    position: absolute; right: 0; top: 0; bottom: 0; width: 154px;
    background: var(--green-mist); color: var(--ink-green);
    text-align: center; padding-top: 98px; font-size: 8px; line-height: 1.35;
  }
  .card-back--round .card-back__panel { width: 140px; padding-top: 86px; font-size: 7px; }
  .card-back__name { font-size: 11px; }
  .card-back__title { color: #4d7f15; }
  .card-back__address { margin-top: 8px; font-style: normal; }
  .brand--small .brand__name { font-size: 18px; }
  .brand--small .brand__suffix { font-size: 6px; letter-spacing: 4px; }
  .brand--small .brand__mark { width: 12px; height: 12px; }

  /* letterhead */
  .letterhead { left: 472px; top: 33px; width: 528px; height: 730px; }
  .letterhead .brand { position: absolute; left: 20px; top: 16px; }
  .letterhead .brand__name { font-size: 30px; }
  .letterhead .brand__mark { width: 20px; height: 20px; }
  .letterhead__swoosh { position: absolute; left: 0; bottom: 0; }
  .letterhead__contact {
    position: absolute; right: 14px; bottom: 18px; text-align: right;
    color: #fff; font-size: 9px; line-height: 1.4; font-style: normal;
  }

  /* envelope */
  .envelope {
    left: 733px; top: 153px; width: 442px; height: 248px;
    background: linear-gradient(to bottom, #cfe99a 0%, #fff 30%, #f4fae9 48%, #b4dc5e 74%, var(--green-bright) 100%);
  }
  .envelope__flap { position: absolute; left: 0; top: 0; }
  .envelope .brand { position: absolute; left: 20px; top: 58px; }
  .envelope__window { position: absolute; left: 253px; top: 145px; width: 150px; height: 72px; background: #fff; }
</style>
</head>
<body>

  <!-- Square business card: front -->
  <section class="piece card-front card-front--square" aria-label="Business card front">
    <div class="brand">
      <span class="brand__mark"></span>
      <span class="brand__text"><span class="brand__name">bramwick carto</span><span class="brand__suffix">Limited</span></span>
    </div>
  </section>

  <!-- Square business card: back -->
  <section class="piece card-back card-back--square" aria-label="Business card back">
    <div class="card-back__band brand brand--small">
      <span class="brand__mark"></span>
      <span class="brand__text"><span class="brand__name">bramwick carto</span><span class="brand__suffix">Limited</span></span>
    </div>
    <div class="card-back__panel">
      <div class="card-back__name">Owen Ferris</div>
      <div class="card-back__title">Director</div>
      <div>0770090045</div>
      <div>hello@bramwickcarto.co.uk</div>
      <address class="card-back__address">17 mill brae road, Larkfield.<br>County Down BT99 4QX</address>
    </div>
  </section>

  <!-- Rounded business card: front -->
  <section class="piece card-front card-front--round" aria-label="Rounded business card front">
    <div class="brand">
      <span class="brand__mark"></span>
      <span class="brand__text"><span class="brand__name">bramwick carto</span><span class="brand__suffix">Limited</span></span>
    </div>
  </section>

  <!-- Rounded business card: back -->
  <section class="piece card-back card-back--round" aria-label="Rounded business card back">
    <div class="card-back__band brand brand--small">
      <span class="brand__mark"></span>
      <span class="brand__text"><span class="brand__name">bramwick carto</span><span class="brand__suffix">Limited</span></span>
    </div>
    <div class="card-back__panel">
      <div class="card-back__name">Owen Ferris</div>
      <div class="card-back__title">Director</div>
      <div>0770090045</div>
      <div>hello@bramwickcarto.co.uk</div>
      <address class="card-back__address">17 mill brae road, Larkfield.<br>County Down BT99 4QX</address>
    </div>
  </section>

  <!-- A4 letterhead -->
  <section class="piece letterhead" aria-label="Letterhead">
    <div class="brand">
      <span class="brand__mark"></span>
      <span class="brand__text"><span class="brand__name">bramwick carto</span><span class="brand__suffix">Limited</span></span>
    </div>
    <svg class="letterhead__swoosh" width="528" height="240" viewBox="0 0 528 240" aria-hidden="true">
      <path d="M528 0 C470 120 300 215 40 240 L528 240 Z" fill="#d5eab0"/>
      <path d="M528 40 C460 140 320 215 90 240 L528 240 Z" fill="#a9d45c"/>
      <path d="M528 85 C450 170 330 220 150 240 L528 240 Z" fill="#79b52b"/>
      <path d="M528 130 C460 190 380 225 260 240 L528 240 Z" fill="#5f9a1c"/>
    </svg>
    <address class="letterhead__contact">
      07700900452<br>
      email hello@bramwickcarto.co.uk<br>
      17 mill brae road, Larkfield<br>
      County Down BT99 4QX
    </address>
  </section>

  <!-- DL envelope -->
  <section class="piece envelope" aria-label="Envelope">
    <svg class="envelope__flap" width="442" height="60" viewBox="0 0 442 60" aria-hidden="true">
      <path d="M0 0 H442 V48 L14 52 L0 46 Z" fill="#9dd21f"/>
    </svg>
    <div class="brand">
      <span class="brand__mark"></span>
      <span class="brand__text"><span class="brand__name">bramwick carto</span><span class="brand__suffix">Limited</span></span>
    </div>
    <div class="envelope__window"></div>
  </section>

</body>
</html>
```